Marrowind Unified Care Brochures (2)

We need two brochures about whiplash treatment to be designed. One is for referring physicians, the other is for the patients they refer. I'd like a few design elements to tie the two together, but also have them be easily distinguishable from one another.
In our region we are considered the top soft tissue injury clinic. We are trying to increase the awareness of our referring physicians to the fact that we have an exceptional rate of success treating acceleration/deceleration injuries from motor vehicle accidents.
We understand the emotional toll of whiplash. We understand how pain robs people of their vitality and motivation. We help victims of whiplash reclaim their health and vitality.
We use Quickleafpress.com for our printing.
Logo, trifold brochure template, and text(pdf files) have been up;oaded to this project.
The text we have provided is what we want. There are two versions of it. One is for the brochure for patients, and one is for the brochure for doctors.

Target Market(s)

Physicians that will refer Whiplash victims to our clinic for soft tissue injury treatment.

Industry/Entity Type

Health

Font styles to use
Serif

Requirements
Must have
• professional graphics that compliment the text.
• All AI files, graphic files etc.
• Colors that work with the Logo.
• Fonts for company name can be found on our website: www.marrowindunifiedcare.example
Nice to have
• We'd like it to have a nice visual flow. We have only provided the text we want. Titles can be different if the design choices would make sense with better titles. We want it to be convincing and calming, and project our sensitivity to those suffering and also prject our confidence in our long history of curing the condition.

```html
<!DOCTYPE html>
<html lang="en">
<head>
<meta charset="utf-8">
<title>Marrowind Unified Care – Whiplash Trifold</title>
<link rel="stylesheet" href="https://fonts.googleapis.com/css2?family=Open+Sans:wght@400;600;700&family=Oswald:wght@500;700&display=swap">
<style>
  :root{
    --brand-blue:#1ba3e3;
    --light-blue:#6fd0f5;
    --deep-blue:#0c86c9;
    --ink:#2b2b2b;
    --white:#ffffff;
    --pill-grey:#5c5c5c;
    --stage:#e4e7ea;
    --body:"Open Sans", Arial, sans-serif;
    --display:"Oswald", "Arial Narrow", sans-serif;
  }
  *{box-sizing:border-box;margin:0;padding:0}
  html,body{width:1200px;height:1121px;overflow:hidden;background:var(--stage);font-family:var(--body)}
  .spread{position:absolute;left:250px;width:700px;height:543px;background:var(--white);overflow:hidden;box-shadow:0 2px 8px rgba(0,0,0,.18)}
  .spread--outside{top:10px}
  .spread--inside{top:568px}
  .shapes{position:absolute;inset:0;width:700px;height:543px}
  .photo{position:absolute}
  .panel{position:absolute;top:0;width:233.33px;height:543px}
  .p1{left:0}.p2{left:233.33px}.p3{left:466.66px}

  .brand{position:absolute;left:0;right:0;text-align:center;color:var(--brand-blue)}
  .brand__dot{display:block;margin:0 auto 8px;border-radius:50%;background:var(--brand-blue)}
  .brand__name{font-family:var(--body);font-weight:600;font-size:13px;letter-spacing:.1px}

  .url-pill{position:absolute;left:15px;right:15px;bottom:0;height:34px;border-radius:8px 8px 0 0;
    background:linear-gradient(#ffffff,#e6e6e6);color:var(--pill-grey);font-size:10.5px;text-align:center;line-height:34px;white-space:nowrap;overflow:hidden}

  .intro-copy{position:absolute;left:20px;right:18px;top:342px;color:var(--white);font-size:10px;line-height:14px;text-align:justify}

  .contact{position:absolute;left:0;right:0;top:397px;text-align:center;color:var(--white);font-size:11px;line-height:16px}
  .contact li{list-style:none}
  .contact svg{vertical-align:-1px;margin-right:5px}
  .contact__social{display:flex;justify-content:center;gap:9px;margin-top:8px}
  .contact__social span{width:8px;height:8px;border-radius:50%;background:rgba(255,255,255,.85)}

  .tagline{position:absolute;left:0;right:0;top:412px;text-align:center;color:var(--white);font-size:16px;line-height:21px}
  .tagline strong{display:block;font-family:var(--display);font-weight:700;font-size:40px;line-height:46px;letter-spacing:.5px}

  .heading-blue{font-family:var(--display);font-weight:500;color:var(--deep-blue);font-size:17px;line-height:22px}
  .mission{position:absolute;left:12px;right:10px;top:20px}
  .mission p{font-size:8.6px;line-height:11.8px;color:var(--ink);text-align:justify;margin-top:9px}
  .mission p:first-of-type{margin-top:6px}

  .toll{position:absolute;left:10px;right:10px;top:20px;color:var(--white)}
  .toll h2{font-family:var(--display);font-weight:500;text-align:center;font-size:17px;line-height:20px}
  .toll h2 span{display:block;font-size:25px;line-height:32px}
  .toll p{font-size:8.3px;line-height:11.4px;text-align:justify;margin-top:9px}
  .toll p.toll__close{text-align:left;width:165px}

  .symptoms{position:absolute;left:12px;right:10px;top:24px;color:var(--white)}
  .symptoms h2{font-size:10px;line-height:13px;font-weight:700;text-align:center}
  .symptoms__lead{font-size:9px;line-height:12px;margin-top:8px}
  .symptoms ul{list-style:none;display:grid;grid-template-columns:1fr 1fr;column-gap:6px;margin-top:8px}
  .symptoms li{font-size:7.4px;line-height:9.5px;margin-bottom:5.5px;padding-left:11px;position:relative}
  .symptoms li.wide{grid-column:1 / span 2}
  .symptoms li svg{position:absolute;left:0;top:1px}
</style>
</head>
<body>

<section class="spread spread--outside" aria-label="Brochure outside">
  <div class="photo" role="img" aria-label="Photo of a woman in a white shirt holding her neck and lower back outdoors by a grassy coastline" style="left:0;top:0;width:233px;height:320px;background:linear-gradient(180deg,#8ec6ea 0%,#bcd9e6 30%,#c9a98a 55%,#8b8f4f 80%,#6d6a3c 100%)"></div>
  <div class="photo" role="img" aria-label="Photo of a man standing on a rock with arms spread wide overlooking a coastal landscape" style="left:470px;top:120px;width:230px;height:290px;background:linear-gradient(180deg,#9fcbe8 0%,#d7e7ef 35%,#8aa2b4 52%,#7e9a55 72%,#8a7a62 100%)"></div>

  <svg class="shapes" viewBox="0 0 700 543" aria-hidden="true">
    <path d="M0 292 C70 270 160 300 233 318 L233 543 L0 543 Z" fill="var(--white)"/>
    <path d="M0 306 C70 286 160 314 233 332 L233 543 L0 543 Z" fill="var(--brand-blue)"/>
    <path d="M233 312 C300 330 390 345 467 352 L467 543 L233 543 Z" fill="var(--light-blue)"/>
    <path d="M233 324 C300 342 390 356 467 362 L467 543 L233 543 Z" fill="var(--white)"/>
    <path d="M233 334 C300 352 390 366 467 372 L467 543 L233 543 Z" fill="var(--brand-blue)"/>
    <path d="M446 0 C432 100 438 230 467 310 L467 0 Z" fill="var(--light-blue)"/>
    <path d="M456 0 C446 100 450 220 467 280 L467 0 Z" fill="var(--brand-blue)"/>
    <path d="M467 0 L500 0 C470 120 470 280 520 340 C570 385 640 395 700 398 L700 543 L467 543 Z" fill="var(--brand-blue)"/>
    <path d="M492 0 L506 0 C480 120 482 270 528 330 C572 372 640 382 700 384 L700 392 C640 390 570 380 520 336 C470 270 470 120 492 0 Z" fill="var(--light-blue)"/>
  </svg>

  <div class="panel p1">
    <p class="intro-copy">These symptoms can last weeks, months or years. The long term ramifications of untreated whiplash can be unnecessary premature degeneration of disk tissue, bone modeling, and engrained neuromuscular guarding habits that maintain pain and limit function. Untreated whiplash can also be a major contributor to the establishment of a pernicious chronic pain cycle.</p>
    <div class="url-pill">www.marrowindunifiedcare.example</div>
  </div>

  <div class="panel p2">
    <div class="brand" style="top:180px">
      <span class="brand__dot" style="width:44px;height:44px"></span>
      <span class="brand__name">Marrowind Unified Care</span>
    </div>
    <ul class="contact">
      <li><svg width="9" height="9" viewBox="0 0 10 10"><path d="M2 0 L4 2.5 L3 4 C4 6 5 7 6.5 7.5 L8 6.5 L10 8.5 L8.5 10 C4 9.5 .5 6 0 1.5 Z" fill="#fff"/></svg>555.014.3730</li>
      <li><svg width="10" height="9" viewBox="0 0 10 9"><rect x="0" y="3" width="10" height="6" rx="1" fill="#fff"/><rect x="2" y="0" width="6" height="4" fill="#fff"/></svg>(555)014-2371</li>
      <li><svg width="7" height="10" viewBox="0 0 7 10"><path d="M3.5 0 C1.5 0 0 1.5 0 3.5 C0 6 3.5 10 3.5 10 C3.5 10 7 6 7 3.5 C7 1.5 5.5 0 3.5 0 Z" fill="#fff"/></svg>4410 Marrowind Way NE Suite<br>204 Marrowind,<br>WA 98000</li>
      <li class="contact__social"><span></span><span></span><span></span><span></span></li>
    </ul>
    <div class="url-pill">www.marrowindunifiedcare.example</div>
  </div>

  <div class="panel p3">
    <div class="brand" style="top:16px">
      <span class="brand__dot" style="width:50px;height:50px"></span>
      <span class="brand__name">Marrowind Unified Care</span>
    </div>
    <p class="tagline">We can help<br>Whiplash sufferers reclaim<strong>THEIR LIVES</strong></p>
    <div class="url-pill">www.marrowindunifiedcare.example</div>
  </div>
</section>

<section class="spread spread--inside" aria-label="Brochure inside">
  <svg class="shapes" viewBox="0 0 700 543" aria-hidden="true">
    <rect x="233.33" y="0" width="466.67" height="543" fill="var(--brand-blue)"/>
    <rect x="466.66" y="0" width="1" height="543" fill="var(--deep-blue)" opacity=".4"/>
  </svg>
  <div class="photo" role="img" aria-label="Photo of a woman running along a sunlit dirt trail between trees" style="left:0;top:405px;width:233px;height:138px;background:linear-gradient(180deg,#f1e7c8 0%,#9bb36a 40%,#5f7a3a 70%,#6a4a2e 100%)"></div>
  <div class="photo" role="img" aria-label="Photo of a smiling woman with arms raised holding a flowing white shawl" style="left:400px;top:440px;width:66px;height:103px;background:linear-gradient(160deg,rgba(255,255,255,.75) 0%,rgba(230,240,248,.45) 60%,rgba(27,163,227,0) 100%)"></div>
  <div class="photo" role="img" aria-label="Photo of a mountain biker riding through a green forest trail" style="left:466.66px;top:320px;width:233.34px;height:223px;background:linear-gradient(180deg,#b9d48a 0%,#6f9a3e 45%,#3f6b26 80%,#5a4a2a 100%)"></div>
  <svg class="shapes" viewBox="0 0 700 543" aria-hidden="true">
    <path d="M466.66 260 L466.66 290 C520 335 620 345 700 320 L700 260 Z" fill="var(--brand-blue)"/>
    <path d="M466.66 290 C520 335 620 345 700 320 L700 332 C620 360 520 352 466.66 304 Z" fill="var(--white)"/>
  </svg>

  <div class="panel p1">
    <div class="mission">
      <h2 class="heading-blue">Our Approach is in Our Mission</h2>
      <p>To Heal: We work to alleviate the symptoms and the neuromuscular problems that cause the symptoms. From the short term goal of defeating the initial pain due to inflammation, to the long term goal of correcting the structural imbalance caused by muscle guarding, we strive to return the patient to a pain free functional state.</p>
      <p>To Educate: Our patients gain a deeper understanding of how the human body works through treatment, movement, stretching, and witnessing the process of healing first hand. Many patients consider the knowledge gained from treatment at our clinic as an unanticipated silver lining.</p>
      <p>To Empower: Through the knowledge gained during the process of treatment at our facility, our patients are empowered, not only to avoid pain and dysfunction, but, more importantly, to move towards ever greater health.</p>
      <p>We have earned and will work to keep the trust of referring Doctors, Physical Therapists, and other referring providers in the South Harrowmere / North Kellin County area.</p>
      <p>We have successfully treated thousands of whiplash cases and look forward to putting our expertise to work for you and your patients.</p>
    </div>
  </div>

  <div class="panel p2">
    <div class="toll">
      <h2>The Emotional Toll of<span>“The Invisible Injury”</span></h2>
      <p>Suffering from a whiplash injury can have far reaching affects. Many whiplash patients have reported to us that the condition causes a strain on the most important relationships in their lives. When spouses, children, friends and co-workers don't understand the whiplash victim's pain or their change in temperament, the social implications are clear. Since the injury is invisible (no casts or crutches), those in the injured person's life may not understand the significance of the injury, which can lead to frustration and stress in relationships at home and at work. Many whiplash victims report that it is often the little things they cannot do, like laundry, house chores, computer work, and dressing themselves, etc., that cause the most stress. Feelings of fragility, fear, anger, vulnerability, guilt, shame, weakness, and victimization are common. It is also common for them to feel misunderstood, isolated, and alone in their suffering.</p>
      <p>Most whiplash sufferers don't want to be seen as complainers, and so are often under diagnosed with only neck pain and headaches, which are usually the most immediately recognizable symptoms.</p>
      <p class="toll__close">Whiplash victims need not despair. Our group of highly trained and experienced professionals at Marrowind Unified Care, LLC have a proven record of successfully treating this condition. We specialize in the treatment of whiplash.</p>
    </div>
  </div>

  <div class="panel p3">
    <div class="symptoms">
      <h2>Massage for Whiplash Soft tissue injury treatment at Marrowind Unified Care We know whiplash, and how to treat it</h2>
      <p class="symptoms__lead">The most common symptoms associated with whiplash:</p>
      <ul>
        <li><svg width="7" height="6" viewBox="0 0 7 6"><path d="M0 3 L2.5 5.5 L7 0.5" stroke="#fff" stroke-width="1.2" fill="none"/></svg>Headache</li>
        <li><svg width="7" height="6" viewBox="0 0 7 6"><path d="M0 3 L2.5 5.5 L7 0.5" stroke="#fff" stroke-width="1.2" fill="none"/></svg>Neck Pain</li>
        <li><svg width="7" height="6" viewBox="0 0 7 6"><path d="M0 3 L2.5 5.5 L7 0.5" stroke="#fff" stroke-width="1.2" fill="none"/></svg>Shoulder Pain</li>
        <li><svg width="7" height="6" viewBox="0 0 7 6"><path d="M0 3 L2.5 5.5 L7 0.5" stroke="#fff" stroke-width="1.2" fill="none"/></svg>Upper Back Pain</li>
        <li><svg width="7" height="6" viewBox="0 0 7 6"><path d="M0 3 L2.5 5.5 L7 0.5" stroke="#fff" stroke-width="1.2" fill="none"/></svg>Mid Back Pain</li>
        <li><svg width="7" height="6" viewBox="0 0 7 6"><path d="M0 3 L2.5 5.5 L7 0.5" stroke="#fff" stroke-width="1.2" fill="none"/></svg>Low Back Pain</li>
        <li class="wide"><svg width="7" height="6" viewBox="0 0 7 6"><path d="M0 3 L2.5 5.5 L7 0.5" stroke="#fff" stroke-width="1.2" fill="none"/></svg>Arm/Hand Numbness, and Pain</li>
        <li class="wide"><svg width="7" height="6" viewBox="0 0 7 6"><path d="M0 3 L2.5 5.5 L7 0.5" stroke="#fff" stroke-width="1.2" fill="none"/></svg>Jaw (TMJ) Pain and Dysfunction</li>
        <li class="wide"><svg width="7" height="6" viewBox="0 0 7 6"><path d="M0 3 L2.5 5.5 L7 0.5" stroke="#fff" stroke-width="1.2" fill="none"/></svg>Sciatica (Pain down legs)</li>
        <li class="wide"><svg width="7" height="6" viewBox="0 0 7 6"><path d="M0 3 L2.5 5.5 L7 0.5" stroke="#fff" stroke-width="1.2" fill="none"/></svg>Slouching Posture</li>
        <li class="wide"><svg width="7" height="6" viewBox="0 0 7 6"><path d="M0 3 L2.5 5.5 L7 0.5" stroke="#fff" stroke-width="1.2" fill="none"/></svg>Rigid Posture</li>
        <li class="wide"><svg width="7" height="6" viewBox="0 0 7 6"><path d="M0 3 L2.5 5.5 L7 0.5" stroke="#fff" stroke-width="1.2" fill="none"/></svg>TBI (Traumatic Brain Injury - from coup-counter coup or head strike)</li>
        <li class="wide"><svg width="7" height="6" viewBox="0 0 7 6"><path d="M0 3 L2.5 5.5 L7 0.5" stroke="#fff" stroke-width="1.2" fill="none"/></svg>Brain Inflammation resulting in memory issues</li>
        <li class="wide"><svg width="7" height="6" viewBox="0 0 7 6"><path d="M0 3 L2.5 5.5 L7 0.5" stroke="#fff" stroke-width="1.2" fill="none"/></svg>PTSD (flinching, anxiety, emotional upset) in traffic, etc.</li>
      </ul>
    </div>
  </div>
</section>

</body>
</html>
```